Satin Decor Paint Label

We will have three different sizes for this label but the dimensions for the medium size are 2" tall by 11.75'' wide. Please work off that.

Our colors are typically black and white but feel free to incorporate silver, gold, bronze or any combination. We would like to see multiple color variations of your designs.

General Info needed on label:
2736
Coatings
Interior Decor Paint
Furniture, Trim, Cabinets
Acrylic Waterborne Urethane
Satin Finish
16 FL. OZ. - 473 mL
````````````````````````````````````````````````````````````````````````````````````````````
Your design does not have to be the same as the one in the attached image.

You can put Satin Finish or Interior Decor Paint or something else going vertically up the side.

The label will be on a container like the the one in the attached image. Please have your design work on the same container.

```html
<!DOCTYPE html>
<html lang="en">
<head>
<meta charset="UTF-8">
<title>2736 Coatings – Satin Finish Label</title>
<link href="https://fonts.googleapis.com/css2?family=Montserrat:wght@400;500;600;700&display=swap" rel="stylesheet">
<style>
  :root {
    --page-bg: #eeeeee;
    --label-black: #141414;
    --label-white: #ffffff;
    --band-silver: #d6d6d6;
    --band-ink: #3a3a3a;
  }
  * { margin: 0; padding: 0; box-sizing: border-box; }
  html, body {
    width: 1200px;
    height: 900px;
    overflow: hidden;
    background: var(--page-bg);
    font-family: "Montserrat", Arial, sans-serif;
  }
  .canvas {
    position: relative;
    width: 1200px;
    height: 900px;
  }
  .label {
    position: absolute;
    left: 150px;
    top: 242px;
    width: 900px;
    height: 416px;
    box-shadow: 0 8px 30px rgba(0,0,0,0.12);
  }
  .label-main {
    position: relative;
    height: 350px;
    background: var(--label-black);
    color: var(--label-white);
  }
  .finish-name {
    position: absolute;
    left: 112px;
    bottom: 26px;
    writing-mode: vertical-rl;
    transform: rotate(180deg);
    font-size: 74px;
    font-weight: 600;
    line-height: 0.95;
    letter-spacing: 1px;
    text-transform: uppercase;
  }
  .product-block {
    position: absolute;
    left: 300px;
    top: 78px;
    width: 440px;
    text-align: center;
  }
  .brand-name {
    font-size: 46px;
    font-weight: 500;
    line-height: 1.1;
    text-transform: uppercase;
    white-space: nowrap;
  }
  .product-type {
    margin-top: 52px;
    font-size: 25px;
    font-weight: 500;
    line-height: 1.1;
    text-transform: uppercase;
  }
  .product-base {
    margin-top: 24px;
    font-size: 21px;
    font-weight: 700;
    letter-spacing: 0.5px;
    text-transform: uppercase;
    white-space: nowrap;
  }
  .label-band {
    height: 66px;
    background: var(--band-silver);
    color: var(--band-ink);
    text-align: center;
    padding-top: 10px;
    text-transform: uppercase;
  }
  .uses {
    font-size: 21px;
    font-weight: 500;
    letter-spacing: 2px;
  }
  .volume {
    font-size: 14px;
    font-weight: 500;
    letter-spacing: 1px;
    margin-top: 4px;
  }
</style>
</head>
<body>
  <div class="canvas">
    <div class="label">
      <div class="label-main">
        <div class="finish-name">Satin<br>Finish</div>
        <div class="product-block">
          <div class="brand-name">2736 Coatings</div>
          <div class="product-type">Interior Decor<br>Paint</div>
          <div class="product-base">Acrylic Waterborne Urethane</div>
        </div>
      </div>
      <div class="label-band">
        <div class="uses">Furniture - Trim - Cabinets</div>
        <div class="volume">16 fl. oz. - 473 mL.</div>
      </div>
    </div>
  </div>
</body>
</html>
```